Larkfield Circuitry LLC is a Minneapolis / St Paul and surrounding communities computer repair and service company. It serves residential and small businesses. We work primarily with virus removal, data recovery, system baselines, networking, and new system installation. The site should look clean, professional, and easy to navigate.

This wordpress project must be coded and integrated into a wordpress theme for easy upload and maintenance.
Updates

Designers - Please make sure your design is in a wordpress theme so that It can be uploaded.  

Thank you,

Brin 

Target Market(s)

Residential and Small Business

Industry/Entity Type

Residential

Requirements
Must have
• Site Content
1. Main Page should have photos that scroll across, Business Description, Space to run
“Specials” Ads
a. Intuitive Navigation
2. Additional Pages
a. Blog for Computer Repair Articles
b. Testimonials Page
c. Contact Pages
d. Services Page with the ability to put in pricing
3. The site must be clean and professional.
4. Wordpress Theme

```html
<!DOCTYPE html>
<html lang="en">
<head>
<meta charset="utf-8">
<title>Larkfield Circuitry LLC – Service</title>
<link href="https://fonts.googleapis.com/css2?family=Lato:wght@400;700;900&display=swap" rel="stylesheet">
<style>
:root{
  --page-bg:#d9dccd;
  --nav-dark:#3f3f3f;
  --nav-darker:#333;
  --green:#55a02a;
  --green-dark:#468a20;
  --ink:#222;
  --muted:#666;
  --rule:#c9c9c9;
  --link-blue:#1d7fc1;
  --footer-bg:#33393b;
  --footer-text:#d0d4d5;
  --ad-red:#d42f34;
  --ad-blue:#1d4f9c;
  --white:#fff;
}
*{box-sizing:border-box;margin:0;padding:0}
html,body{width:1069px;height:1200px;overflow:hidden}
body{background:var(--page-bg);font-family:"Lato",Arial,sans-serif;color:var(--ink);position:relative}
.abs{position:absolute}
.nav-band{left:0;top:88px;width:1069px;height:107px;background:linear-gradient(#474747,#3a3a3a)}
.brand{left:126px;top:9px;display:flex;align-items:center;gap:12px}
.brand-mark{width:64px;height:64px;border-radius:50%;border:5px solid var(--green)}
.brand-name{font-size:29px;font-weight:700;color:#555}
.contact-top{left:666px;font-size:18px;color:#444;display:flex;align-items:center;gap:13px}
.contact-top.email{font-size:12.5px;color:var(--green-dark)}
.contact-top svg{flex:none}
.main-nav{left:132px;top:100px;display:flex;list-style:none}
.main-nav li{color:var(--white);font-weight:700;font-size:14.5px;margin-right:23px}
.search{left:707px;top:100px;width:230px;height:21px;background:var(--white);border-radius:11px;overflow:hidden}
.search-btn{position:absolute;right:0;top:0;width:56px;height:21px;background:linear-gradient(#f4f4f4,#d9d9d9);font-size:11.5px;text-align:center;line-height:21px;border-left:1px solid #bbb}
.content{left:117px;top:133px;width:834px;height:922px;background:var(--white);border-radius:4px}
.hero-frame{left:124px;top:140px;width:820px;height:198px;border:1px solid #ddd;border-radius:4px}
.hero{left:130px;top:146px;width:809px;height:131px;background:linear-gradient(120deg,#8fb3de,#3a6eb8 45%,#10336e)}
.hero-title{right:8px;top:40px;color:var(--white);text-align:left;width:230px}
.hero-title b{display:block;font-size:33px;font-weight:900;line-height:1}
.hero-title span{display:block;font-size:28px;font-weight:400;line-height:1.05}
.page-title{left:130px;top:278px;width:809px;height:54px;background:var(--green);color:var(--white);font-size:21px;font-weight:400;padding-left:15px;line-height:54px}
.section-head{left:141px;width:504px;font-size:14.5px;font-weight:700;padding-bottom:8px;border-bottom:1px dashed var(--rule)}
.services{left:141px;top:385px;list-style:none;font-size:12px;color:var(--muted)}
.services li{height:20.9px;line-height:20.9px;padding-left:9px;position:relative}
.services li::before{content:"›";position:absolute;left:0;color:var(--green);font-weight:900}
.services b{font-weight:400;color:var(--ink)}
.intro{left:141px;top:693px;width:504px;font-size:12px;line-height:17px;color:var(--muted)}
.prices{left:141px;top:749px;width:505px;border-collapse:separate;border-spacing:0;font-size:12px}
.prices th{height:36px;font-size:12.5px}
.prices th.service-col{text-align:left;vertical-align:bottom;padding-bottom:6px;font-weight:700}
.prices th.rate-col{background:var(--green);color:var(--white);font-weight:700;line-height:13px;vertical-align:top;text-align:center;padding:5px 12px 0;border-radius:3px 3px 0 0}
.prices td{height:25.8px;border-bottom:1px solid #e6e6e6;color:var(--muted)}
.prices td.num{text-align:center;color:var(--ink);border-left:1px solid #e6e6e6;border-right:1px solid #e6e6e6}
.prices .gap{width:8px;border:none}
.sidebar{left:664px;top:362px;width:272px;height:492px;background:#f1f1f1;border:1px solid #ddd;border-radius:4px}
.ad{left:675px;top:372px;width:249px;height:208px;background:#eef3f9;border:4px solid var(--ad-red);text-align:center}
.ad-q{margin-top:14px;color:var(--ad-red);font-size:28px;font-weight:900;line-height:34px}
.ad-brand{margin:10px auto 0;width:208px;height:45px;background:var(--ad-blue);border-radius:5px;color:var(--white);font-size:22px;font-weight:900;line-height:45px}
.ad-sub{margin-top:6px;color:var(--ad-blue);font-size:16px;font-weight:900}
.ad-price{color:var(--ad-red);font-size:15px;font-style:italic}
.blog-head{left:675px;top:594px;width:250px;height:33px;background:var(--green);color:var(--white);font-size:14px;font-weight:700;padding-left:12px;line-height:33px;border-radius:3px}
.post{left:675px;top:634px;width:250px;font-size:12px}
.post-title{color:var(--link-blue);line-height:14px;margin-bottom:6px}
.post-meta{color:#888;font-size:11px}
.post-author{color:var(--ink);margin:2px 0 7px}
.post-date{color:var(--ink);margin-bottom:5px}
.post-body{color:var(--muted);line-height:17px;padding-left:3px}
.view-all{color:var(--green-dark);margin-top:5px;padding-left:3px}
.footer{left:117px;top:1057px;width:834px;height:129px;background:var(--footer-bg);color:var(--footer-text);font-size:12px;border-radius:0 0 4px 4px}
.footer h4{color:var(--white);font-size:12.5px;font-weight:700;margin-bottom:9px}
.f-col{position:absolute;top:14px}
.f-links{display:grid;grid-template-columns:84px 80px;row-gap:4px;list-style:none}
.f-contact p{line-height:17px}
.f-social li{list-style:none;display:flex;align-items:center;gap:11px;margin-bottom:9px}
.f-social .sq{width:19px;height:19px;background:#4f7fb0;border-radius:2px}
.f-legal p{line-height:16px}
</style>
</head>
<body>
<div class="abs nav-band"></div>

<header>
  <div class="abs brand"><span class="brand-mark"></span><span class="brand-name">Larkfield Circuitry LLC</span></div>
  <div class="abs contact-top" style="top:26px">
    <svg width="18" height="18" viewBox="0 0 18 18"><rect width="18" height="18" rx="3" fill="#55a02a"/><path d="M5 4c1-.6 1.6 0 2.2 1.3.5 1 .2 1.4-.4 1.9.6 1.6 1.6 2.6 3.2 3.3.5-.6.9-.9 1.9-.4 1.3.6 1.9 1.2 1.3 2.2-.8 1.4-2.3 1.4-4 .6C6.5 11.7 4.8 10 4.1 7.4 3.7 5.9 4 4.7 5 4z" fill="#fff"/></svg>
    <span>651-555-0148</span>
  </div>
  <div class="abs contact-top email" style="top:59px">
    <svg width="18" height="14" viewBox="0 0 18 14"><rect width="18" height="14" rx="2" fill="#55a02a"/><path d="M2 3l7 5 7-5" stroke="#fff" stroke-width="1.6" fill="none"/></svg>
    <span>CustomerService@LarkfieldCircuitry.com</span>
  </div>
  <ul class="abs main-nav">
    <li>Home</li><li>About Us</li><li>Services</li><li>Products</li><li>Blog</li><li>Testimonials</li><li>Contact Us</li>
  </ul>
  <div class="abs search">
    <svg class="abs" style="left:8px;top:5px" width="11" height="11" viewBox="0 0 11 11"><circle cx="4.5" cy="4.5" r="3.3" stroke="#888" stroke-width="1.6" fill="none"/><path d="M7 7l3 3" stroke="#888" stroke-width="1.8"/></svg>
    <div class="search-btn">Search</div>
  </div>
</header>

<main>
  <div class="abs content"></div>
  <div class="abs hero-frame"></div>
  <div class="abs hero" role="img" aria-label="Close-up photograph of a blue circuit board">
    <div class="abs hero-title"><b>LOREM IPSUM</b><span>DOLOR SIT AMET</span></div>
  </div>
  <h1 class="abs page-title">Service</h1>

  <h2 class="abs section-head" style="top:352px">Our computer repair services</h2>
  <ul class="abs services">
    <li><b>Malware Removal</b> - Remove &amp; proactively block computer viruses, spyware, and adware.</li>
    <li><b>Computer Tuneup</b> - Dust removal, software updates, and hard drive defragmentation.</li>
    <li><b>Upgrades</b> - Install more memory or a larger hard drive.</li>
    <li><b>Slow Computer</b> - Locate and fix bottlenecks slowing your computer.</li>
    <li><b>Blue Screens</b> - Random crashes, system doesn't start.</li>
    <li><b>Hardware Troubleshooting</b> - Computer doesn't turn on, shuts off, or reboots.</li>
    <li><b>Software Troubleshooting</b> - Analyze symptoms to fix application and driver crashes.</li>
    <li><b>Wireless Networking (WiFi)</b> - Installation, extend wireless range, and setting up encryption.</li>
    <li><b>Operating System Install</b> - Installing Orbit OS 5 or Orbit OS 6.</li>
    <li><b>Networking</b> - Share your printer and files with other computers.</li>
    <li><b>Install Gadgets</b> - Troubleshoot devices such as your camera, pocket phone or scanner.</li>
    <li><b>On-site/In-shop service</b> - We make house calls or you can bring the computer to us.</li>
  </ul>

  <h2 class="abs section-head" style="top:661px">How much it costs</h2>
  <p class="abs intro">If you jumped straight to this section then you're just like us - what's the bottom line? We want our computer services to be as affordable and competitive as possible, we're cheap geeks. Here are some example prices along with a comparison:</p>

  <table class="abs prices">
    <thead>
      <tr><th class="service-col">Service</th><th class="rate-col" style="width:76px">Our Rate</th><th class="gap"></th><th class="rate-col" style="width:77px">Compare to*</th></tr>
    </thead>
    <tbody>
      <tr><td>Lorem ipsum dolor sit amet, consectetur adipiscing elit.</td><td class="num">$75</td><td class="gap"></td><td class="num">$130</td></tr>
      <tr><td>Proin fringilla sapien enim, vel gravida ante.</td><td class="num">$75</td><td class="gap"></td><td class="num">$130</td></tr>
      <tr><td>Donec quis enim ut justo commodo sodales.</td><td class="num">$75</td><td class="gap"></td><td class="num">$130</td></tr>
      <tr><td>Sed rhoncus lectus vel dui blandit auctor</td><td class="num">$75</td><td class="gap"></td><td class="num">$130</td></tr>
      <tr><td>Nulla ut erat lectus, quis mattis lectus.</td><td class="num">$75</td><td class="gap"></td><td class="num">$130</td></tr>
      <tr><td>Morbi gravida consequat nunc, ac congue diam egestas in.</td><td class="num">$75</td><td class="gap"></td><td class="num">$130</td></tr>
      <tr><td>Sed rhoncus lectus vel dui blandit auctor</td><td class="num">$75</td><td class="gap"></td><td class="num">$130</td></tr>
      <tr><td>Nulla ut erat lectus, quis mattis lectus.</td><td class="num">$75</td><td class="gap"></td><td class="num">$130</td></tr>
      <tr><td>Morbi gravida consequat nunc, ac congue diam egestas in.</td><td class="num">$75</td><td class="gap"></td><td class="num">$130</td></tr>
    </tbody>
  </table>

  <aside>
    <div class="abs sidebar"></div>
    <div class="abs ad">
      <div class="ad-q">Cloud Suite<br>expensive?</div>
      <div class="ad-brand">PostVerra</div>
      <div class="ad-sub">Business Email System</div>
      <div class="ad-price">Just $1 per user /mo</div>
    </div>
    <h3 class="abs blog-head">Latest Blog Feeds</h3>
    <article class="abs post">
      <p class="post-title">Lorem ipsum dolor sit amet, consectetur adipiscing elit.</p>
      <p class="post-meta">Posted by:</p>
      <p class="post-author">Marina Holt</p>
      <p class="post-date">03 Aug, 2012</p>
      <p class="post-body">Lorem ipsum dolor sit amet, consectetur adipisicing elit, sed do eiusmod tempor incididunt ut labore et dolore magna aliqua. Ut enim ad minim veniam, quis nostrud exercitation ullamco laboris nisi ut aliquip ex ea commodo consequat.</p>
      <p class="view-all">View All <b>+</b></p>
    </article>
  </aside>
</main>

<footer class="abs footer">
  <div class="f-col" style="left:8px">
    <h4>Quick Navigation</h4>
    <ul class="f-links"><li>Home</li><li>Blog</li><li>About Us</li><li>Testimonials</li><li>Services</li><li>Contact Us</li><li>Products</li></ul>
  </div>
  <div class="f-col f-contact" style="left:190px">
    <h4>Contact Info</h4>
    <p>123 Lorem ipsum dolor</p>
    <p>Some City, P.O 457845, Country</p>
    <p style="margin-top:6px">P:&nbsp; 651-555-0148</p>
    <p>E:&nbsp; CustomerService@LarkfieldCircuitry.com</p>
  </div>
  <div class="f-col f-social" style="left:472px">
    <h4>Connect with us</h4>
    <ul><li><span class="sq"></span>Join Us on Circlepage</li><li><span class="sq"></span>Chirper</li></ul>
  </div>
  <div class="f-col f-legal" style="left:647px">
    <h4>© 2012 Larkfield Circuitry L.L.C</h4>
    <p style="margin-top:28px">All right are reserved.</p>
    <p>Terms of Service | Privacy Policy</p>
  </div>
</footer>
</body>
</html>
```